Business Card Design Project

We have 2 businesses which help each other.

Maplewick Care (providing nurses to hospitals/nursing homes etc)

and

Maplewick HR (providing nurses to our maplewick care business - but also providing workers for farms, restaurants meatworks etc)

We would like 2 separate business cards - but similar design and feel

Target Market(s)

Managers of nursing homes, hospitals, farms, meatworks, restauants

Industry/Entity Type

Business

Requirements
Must have
• both logos
https://www.filecrate.example/s/9q2m7t4kzrx8vbn/MaplewickHR-Logo-Horizontal.ai
https://www.filecrate.example/s/kp57wx2nb8y4q1h/73918_215607_88264_sourcefile.ai

You may edit the layout of Maplewick HR logo

Name
position
mobile
Phone
name@maplewickhr.com.au
mapelwickhr.com.au

Name
position
mobile
phone
name@maplewickcare.net.au
maplewickcare.net.au

```html
<!DOCTYPE html>
<html lang="en">
<head>
<meta charset="utf-8">
<title>Maplewick Care – Business Card</title>
<link rel="stylesheet" href="https://fonts.googleapis.com/css2?family=Arimo:wght@400;700&display=swap">
<style>
  :root {
    --backdrop: #2b2b2b;
    --card-paper: #ebeae6;
    --header-top: #ffffff;
    --header-bottom: #f1f1f1;
    --header-edge: #dcdcdc;
    --navy: #2b2f8f;
    --sky: #35a6dc;
    --ink-soft: #3a3f96;
  }
  html, body {
    margin: 0;
    padding: 0;
    width: 1200px;
    height: 800px;
    overflow: hidden;
    background: var(--backdrop);
    font-family: "Arimo", Arial, sans-serif;
  }
  .canvas {
    position: relative;
    width: 1200px;
    height: 800px;
    display: flex;
    align-items: center;
    justify-content: center;
  }
  .business-card {
    position: relative;
    width: 440px;
    height: 720px;
    background: var(--card-paper);
    box-shadow: 0 10px 30px rgba(0,0,0,0.45);
    overflow: hidden;
  }
  .card-header {
    position: absolute;
    left: 0; top: 0;
    width: 100%;
    height: 170px;
    background: linear-gradient(180deg, var(--header-top), var(--header-bottom));
    border-bottom: 12px solid var(--header-edge);
    box-sizing: border-box;
  }
  .person {
    position: absolute;
    right: 34px;
    top: 78px;
    text-align: right;
  }
  .person-name {
    margin: 0;
    font-size: 36px;
    font-weight: 700;
    letter-spacing: 1px;
    color: var(--navy);
  }
  .person-role {
    margin: 2px 0 0;
    font-size: 20px;
    font-weight: 700;
    color: var(--sky);
  }
  .contact-list {
    position: absolute;
    left: 40px;
    top: 230px;
    margin: 0;
    padding: 0;
    list-style: none;
  }
  .contact-item {
    display: flex;
    align-items: center;
    height: 50px;
    color: var(--navy);
  }
  .contact-item svg {
    width: 28px;
    height: 28px;
    margin-right: 22px;
    fill: var(--navy);
  }
  .contact-number { font-size: 25px; letter-spacing: 2px; }
  .contact-text { font-size: 20px; }
  .brand {
    position: absolute;
    left: 0;
    right: 0;
    bottom: 80px;
    display: flex;
    flex-direction: column;
    align-items: center;
  }
  .brand-dot {
    width: 70px;
    height: 70px;
    border-radius: 50%;
    background: var(--sky);
    margin-bottom: 22px;
  }
  .brand-name {
    font-size: 46px;
    font-weight: 700;
    color: var(--ink-soft);
    letter-spacing: -0.5px;
  }
</style>
</head>
<body>
<main class="canvas">
  <article class="business-card">
    <header class="card-header">
      <div class="person">
        <h1 class="person-name">Daniel Harlow</h1>
        <p class="person-role">manager</p>
      </div>
    </header>

    <ul class="contact-list">
      <li class="contact-item">
        <svg viewBox="0 0 24 24" aria-hidden="true"><path d="M7 1h10a2 2 0 0 1 2 2v18a2 2 0 0 1-2 2H7a2 2 0 0 1-2-2V3a2 2 0 0 1 2-2zm1 3v7h8V4H8zm0 9v2h2v-2H8zm3 0v2h2v-2h-2zm3 0v2h2v-2h-2zm-6 3v2h2v-2H8zm3 0v2h2v-2h-2zm3 0v2h2v-2h-2z"/></svg>
        <span class="contact-number">0358 21 407 63</span>
      </li>
      <li class="contact-item">
        <svg viewBox="0 0 24 24" aria-hidden="true"><path d="M2 7c0-2 3-4 10-4s10 2 10 4v2h-5V7c-1-.5-3-1-5-1s-4 .5-5 1v2H2V7zm5 3h10l3 8v3H4v-3l3-8zm5 2.5a3 3 0 1 0 0 6 3 3 0 0 0 0-6z"/></svg>
        <span class="contact-number">0358 21 407 63</span>
      </li>
      <li class="contact-item">
        <svg viewBox="0 0 24 24" aria-hidden="true"><path d="M2 5h20v14H2V5zm2 2v.5l8 6 8-6V7H4zm0 3v7h16v-7l-8 6-8-6z"/></svg>
        <span class="contact-text">name@maplewickhr.com.au</span>
      </li>
      <li class="contact-item">
        <svg viewBox="0 0 24 24" aria-hidden="true"><path d="M12 2a10 10 0 1 0 0 20 10 10 0 0 0 0-20zm-1 2.1V8H7.6A8 8 0 0 1 11 4.1zm2 0A8 8 0 0 1 16.4 8H13V4.1zM5.1 10H11v4H5.1a8 8 0 0 1 0-4zm7.9 0h5.9a8 8 0 0 1 0 4H13v-4zm-5.4 6H11v3.9A8 8 0 0 1 7.6 16zm5.4 0h3.4a8 8 0 0 1-3.4 3.9V16z"/></svg>
        <span class="contact-text">mapelwickhr.com.au</span>
      </li>
    </ul>

    <div class="brand">
      <span class="brand-dot" aria-hidden="true"></span>
      <span class="brand-name">Maplewick Care</span>
    </div>
  </article>
</main>
</body>
</html>
```